label design for oral care product

Kindly invite you to design bottle label (114 mm*40 mm) for our product, a kind of oral care product. The GEL is different from our previous cleanser product, as the pic we uploaded for demonstration. The color of frosted glass bottle is dark green, but the cap is white. You could download the pic of bottle among the uploaded files. The logo file and label content description are attached too. Please check them. Our product is made from many kinds of natural plant extracts, which includes herb and fruit. I wish the label would make our product look high-end and reliable. And it would be better if you could give some advice on paper material and special requirements for printing, related to your design. I value the texture of label too, because I think that stands for the quality of products. No color limitation for the use of our logo.
Target Market(s)
20-40 female, who value oral health.
Colors
Designer to choose colors to be used in the design.
Look and feel
Each slider illustrates characteristics of the customer's brand and the style your logo design should communicate.

```html
<!DOCTYPE html>
<html lang="en">
<head>
<meta charset="utf-8">
<title>Verdine Gel – Bottle Labels</title>
<link rel="stylesheet" href="https://fonts.googleapis.com/css2?family=Lexend:wght@400;500&family=Open+Sans:ital,wght@0,400;1,400&family=Tinos&display=swap">
<style>
  :root {
    --backdrop: #e4e4ea;
    --label-paper: #efeff1;
    --label-edge: #d8d8de;
    --ink-navy: #3b3d6c;
    --ink-body: #4e5078;
    --art-tone-light: #d9dbe8;
    --art-tone-dark: #a9acc8;
  }
  * { box-sizing: border-box; margin: 0; padding: 0; }
  html, body {
    width: 1200px;
    height: 1200px;
    overflow: hidden;
    background: var(--backdrop);
  }
  .label-sheet {
    position: relative;
    width: 1200px;
    height: 1200px;
    display: flex;
    justify-content: center;
    align-items: center;
    gap: 60px;
  }
  .label {
    position: relative;
    width: 480px;
    height: 640px;
    background: var(--label-paper);
    border: 1px solid var(--label-edge);
    border-radius: 14px;
    color: var(--ink-navy);
    display: flex;
    flex-direction: column;
    align-items: center;
    overflow: hidden;
  }
  .label__art {
    width: 300px;
    height: 160px;
    border-radius: 0 0 40px 40px;
    background: linear-gradient(160deg, var(--art-tone-light), var(--art-tone-dark));
  }
  .label__title {
    font-family: "Lexend", sans-serif;
    font-weight: 400;
    font-size: 64px;
    line-height: 1.18;
    letter-spacing: 3px;
    text-align: center;
    text-transform: uppercase;
  }
  .label--front .label__title { margin-top: 14px; }
  .label--back .label__title { margin-top: 38px; }
  .label__claim {
    font-family: "Lexend", sans-serif;
    font-weight: 500;
    font-size: 18px;
    letter-spacing: 1.2px;
    margin-top: 58px;
    text-align: center;
  }
  .label__tagline {
    font-family: "Lexend", sans-serif;
    font-size: 18px;
    line-height: 1.55;
    letter-spacing: 1.2px;
    margin-top: 30px;
    text-align: center;
  }
  .label__volume {
    font-family: "Tinos", serif;
    font-size: 34px;
    margin-top: 56px;
    padding: 2px 14px;
    border: 1px solid var(--ink-navy);
  }
  .label__copy {
    font-family: "Open Sans", sans-serif;
    font-size: 21px;
    line-height: 1.36;
    color: var(--ink-body);
    text-align: justify;
    width: 410px;
    margin-top: 30px;
  }
  .label__copy + .label__copy { margin-top: 24px; }
  .label__copy--last { text-align-last: center; }
  .label__origin {
    position: absolute;
    bottom: 38px;
    font-family: "Open Sans", sans-serif;
    font-style: italic;
    font-size: 20px;
    color: var(--ink-body);
  }
</style>
</head>
<body>
  <main class="label-sheet">
    <section class="label label--front">
      <div class="label__art" role="img" aria-label="Line drawing of mint and herb leaves"></div>
      <h1 class="label__title">Verdine<br>Gel</h1>
      <p class="label__claim">Immune Support for Oral Health</p>
      <p class="label__tagline">the Solution to Maintain Dental<br>Hygiene and Strengthen Gums</p>
      <p class="label__volume">30 ML / 1 fl oz</p>
    </section>

    <section class="label label--back">
      <h2 class="label__title">Verdine<br>Gel</h2>
      <p class="label__copy">Directions: Drop on the teeth directly after brushing. Or, put into clear aligners before wearing again. No need to rinse your mouth with water.</p>
      <p class="label__copy label__copy--last">Contains: a proprietary blend of natural plant extract including Angelica, Radix Rehmanniae, Coptis, Honeysuckle, Echinacea, Sage, Chamomile, Acerola cherry.</p>
      <p class="label__origin">Made in Taiwan</p>
    </section>
  </main>
</body>
</html>
```